KeyBridge needs a modern business card

We are a modern conveyancing company and we need to appeal to the top (Multi-million dollar properties)and bottom on the property conveyancing market but our sweet spot is the middle of the market. I like professional with a hint of unconventional.

Target Market(s)

As above

Industry/Entity Type

Real Estate

Contact Information for Business Card

Back Of card:
thinking black with the logo and a tag line (I could be wrong about the black)
Tag line - Right Expertise, Exceptional Service

Front of Card:
Marissa Doyle (BBus (Finance) LLB)
Licensed Conveyancer
Email: marissa@keybridge.com.au

Key Bridge
ABN: 41 836 907
Suite 14, Level 3, 9 Harlow Avenue Westmead, NSW 2145
Phone: 1300 782 916

Sydney - Melbourne - Brisbane (Perhaps have this along the bottom of the card)

Requirements
Must have
• Sleek, modern and top end appeal (But approachable)
Should not have
• Not too cluttered

```html
<!DOCTYPE html>
<html lang="en">
<head>
<meta charset="utf-8">
<title>KeyBridge Business Card</title>
<link rel="stylesheet" href="https://fonts.googleapis.com/css2?family=Lato:wght@400;700&family=Arimo:wght@400&display=swap">
<style>
  :root {
    --stage-light: #f4f4f4;
    --stage-mid: #d6d6d6;
    --navy: #1f4a70;
    --navy-deep: #234360;
    --sky: #3ec4f0;
    --lime: #a0cd3a;
    --white: #ffffff;
    --label: #959595;
  }
  * { box-sizing: border-box; margin: 0; padding: 0; }
  html, body { width: 1200px; height: 608px; overflow: hidden; }
  body {
    position: relative;
    background: radial-gradient(ellipse 900px 500px at 0 0, var(--stage-light), var(--stage-mid) 70%);
    font-family: "Lato", Arial, sans-serif;
  }
  .card {
    position: absolute;
    top: 145px;
    width: 510px;
    height: 291px;
    box-shadow: 6px 8px 10px rgba(0,0,0,0.28);
  }
  .card--front { left: 96px; background: var(--white); color: var(--navy); }
  .card--back { left: 616px; background: var(--navy-deep); }

  .brand-name {
    position: absolute; left: 42px; top: 32px;
    font-size: 29px; font-weight: 700; letter-spacing: -0.2px;
  }
  .brand-service {
    position: absolute; left: 42px; top: 63px;
    font-size: 12px;
  }
  .person-name {
    position: absolute; left: 42px; top: 88px;
    font-size: 16px; font-weight: 700;
  }
  .person-role {
    position: absolute; left: 42px; top: 108px;
    font-size: 11.5px;
  }
  .contact-row {
    position: absolute; left: 42px;
    display: flex; align-items: flex-start; gap: 5px;
    font-size: 10.4px; line-height: 12.8px;
  }
  .contact-row svg { flex: none; fill: var(--sky); }
  .contact-row--address { top: 135px; }
  .contact-row--address .contact-text { margin-left: 2px; }
  .contact-row--email { top: 196px; }
  .contact-row--phone { top: 218px; }
  .office-cities {
    position: absolute; left: 42px; top: 245px;
    font-size: 15px; font-weight: 700; letter-spacing: 0.1px;
  }

  .back-brand {
    position: absolute; left: 346px; top: 150px;
    display: flex; align-items: center; gap: 7px;
    color: var(--white); font-size: 21px; font-weight: 700;
  }
  .back-brand__square { width: 12px; height: 12px; background: var(--lime); }
  .tagline {
    position: absolute; left: 278px; top: 214px;
    font-family: "Arimo", Arial, sans-serif;
    color: var(--sky); font-size: 18px; line-height: 23px;
    text-transform: uppercase;
  }

  .side-label {
    position: absolute; top: 496px;
    width: 200px; text-align: center;
    color: var(--label); font-size: 17px; letter-spacing: 0.5px;
  }
  .side-label--front { left: 250px; }
  .side-label--back { left: 794px; }
</style>
</head>
<body>
  <section class="card card--front" aria-label="Card front">
    <h1 class="brand-name">KeyBridge</h1>
    <p class="brand-service">Conveyancing Services</p>
    <h2 class="person-name">Marissa Doyle (BBus (Finance) LLB)</h2>
    <p class="person-role">Licensed Conveyancer</p>

    <div class="contact-row contact-row--address">
      <svg width="10" height="14" viewBox="0 0 10 14" aria-hidden="true">
        <path d="M5 0C2.2 0 0 2.2 0 5c0 3.6 5 9 5 9s5-5.4 5-9C10 2.2 7.8 0 5 0zm0 7a2 2 0 1 1 0-4 2 2 0 0 1 0 4z"/>
      </svg>
      <p class="contact-text">Key Bridge<br>ABN: 41 836 907<br>Suite 14, Level 3, 9 Harlow Avenue<br>Westmead, NSW 2145</p>
    </div>
    <div class="contact-row contact-row--email">
      <svg width="12" height="9" viewBox="0 0 12 9" aria-hidden="true">
        <path d="M0 0h12v9H0z M0.8 0.8 6 5 11.2 0.8" stroke="#fff" stroke-width="0.9"/>
      </svg>
      <p class="contact-text">marissa@keybridge.com.au</p>
    </div>
    <div class="contact-row contact-row--phone">
      <svg width="12" height="10" viewBox="0 0 12 10" aria-hidden="true">
        <path d="M0 3C0 1 2 0 6 0s6 1 6 3v1H9V2.5H3V4H0z M2.5 5 4 3h4l1.5 2v5h-7z"/>
      </svg>
      <p class="contact-text">1300 782 916</p>
    </div>
    <p class="office-cities">SYDNEY - MELBOURNE - BRISBANE</p>
  </section>

  <section class="card card--back" aria-label="Card back">
    <div class="back-brand">
      <span class="back-brand__square" aria-hidden="true"></span>
      <span class="back-brand__name">KeyBridge</span>
    </div>
    <p class="tagline">Right expertise,<br>exceptional service</p>
  </section>

  <p class="side-label side-label--front">FRONT</p>
  <p class="side-label side-label--back">BACK</p>
</body>
</html>
```